New Billboard Design Project

I would like a billboard with the attached image of me Vectored onto it. With my name Marcus Thornley

also the attached logo

Maybe saying "WELCOME TO BRIGHTMEADOW" large across the top.

Real Estate Professional

1.75% FULL listing service

Call/Text 410-937-2815

(Then the text below much smaller because it is required by law)

Office: 833-555-2947
2741 W Harrowgate Rd
Bel Air, MD 21014
www.brightmeadowhomes.com

Billboard size is:

48 FT X 14 FT

```html
<!DOCTYPE html>
<html lang="en">
<head>
<meta charset="utf-8">
<title>Welcome to Brightmeadow – Marcus Thornley</title>
<link href="https://fonts.googleapis.com/css2?family=Montserrat:wght@300;400;500;600;700;800&display=swap" rel="stylesheet">
<style>
  :root {
    --navy: #0f2d5a;
    --navy-deep: #07142e;
    --grey: #9b9b9b;
    --white: #ffffff;
    --paper: #ffffff;
  }
  * { margin: 0; padding: 0; box-sizing: border-box; }
  html, body { width: 886px; height: 1200px; overflow: hidden; background: var(--paper); }
  .billboard {
    position: relative;
    width: 886px;
    height: 1200px;
    overflow: hidden;
    background: var(--paper);
    font-family: "Montserrat", sans-serif;
    color: var(--navy);
  }
  .headline { position: absolute; left: 0; top: 0; width: 886px; height: 260px; }
  .headline text { font-family: "Montserrat", sans-serif; font-weight: 800; font-size: 98px; }
  .headline .accent { fill: var(--grey); }
  .headline .main { fill: var(--navy); }

  .portrait {
    position: absolute;
    left: 470px; top: 278px;
    width: 416px; height: 922px;
    border-radius: 190px 190px 0 0;
    background: linear-gradient(180deg, #c79a82 0%, #e7e3ea 30%, #2f3d5c 48%, #27324d 100%);
  }

  .offer-badge {
    position: absolute;
    left: 59px; top: 289px;
    width: 348px; height: 348px;
    border-radius: 50%;
    background: var(--navy);
    color: var(--white);
    text-align: center;
  }
  .offer-rate {
    position: absolute; left: 0; right: 0; top: 98px;
    font-size: 104px; font-weight: 700; letter-spacing: -4px; line-height: 1;
    padding-left: 12px;
  }
  .offer-rate .pct { font-weight: 300; letter-spacing: 0; }
  .offer-text {
    position: absolute; left: 0; right: 0; top: 212px;
    font-size: 39px; font-weight: 400; line-height: 41px;
  }

  .agent { position: absolute; left: 55px; top: 690px; }
  .agent-name { font-size: 41px; font-weight: 700; line-height: 44px; letter-spacing: -0.3px; }
  .agent-title { font-size: 24px; font-weight: 400; line-height: 26px; }

  .contact-band { position: absolute; left: 0; top: 780px; width: 886px; height: 159px; }
  .band-label {
    position: absolute; left: 0; top: 0; width: 228px; height: 159px;
    background: var(--grey); color: var(--white);
  }
  .band-label span {
    position: absolute; left: 58px; top: 30px;
    font-size: 54px; font-weight: 700; line-height: 48px; letter-spacing: -1.5px;
  }
  .band-number { position: absolute; left: 228px; top: 0; width: 658px; height: 159px; }
  .band-number text { font-family: "Montserrat", sans-serif; font-weight: 700; font-size: 96px; fill: var(--white); }

  .brand { position: absolute; left: 56px; top: 962px; width: 162px; text-align: center; }
  .brand-mark { width: 44px; height: 44px; border-radius: 50%; background: var(--navy); margin: 0 auto 10px; }
  .brand-name { font-size: 15px; font-weight: 600; line-height: 17px; color: var(--navy); letter-spacing: 0.5px; text-transform: uppercase; }

  .legal { position: absolute; left: 55px; top: 1097px; font-size: 17px; line-height: 20px; color: var(--navy); }
  .legal strong { font-weight: 700; }
  .legal .web { font-weight: 700; }
</style>
</head>
<body>
<main class="billboard">
  <svg class="headline" viewBox="0 0 886 260" aria-label="Welcome to Brightmeadow">
    <text x="60" y="145" textLength="760" lengthAdjust="spacingAndGlyphs"><tspan class="main">WELCOME </tspan><tspan class="accent">TO</tspan></text>
    <text class="main" x="60" y="235" textLength="762" lengthAdjust="spacingAndGlyphs">BRIGHTMEADOW</text>
  </svg>

  <div class="portrait" role="img" aria-label="Portrait of Marcus Thornley in a navy suit jacket and light shirt"></div>

  <div class="offer-badge">
    <div class="offer-rate">1.75<span class="pct">%</span></div>
    <div class="offer-text">FULL listing<br>service</div>
  </div>

  <div class="agent">
    <div class="agent-name">Marcus Thornley</div>
    <div class="agent-title">Real Estate Professional</div>
  </div>

  <div class="contact-band">
    <div class="band-label"><span>Call/<br>Text</span></div>
    <svg class="band-number" viewBox="0 0 658 159" aria-label="410-937-2815">
      <rect x="0" y="0" width="658" height="159" fill="var(--navy)"/>
      <rect x="97" y="0" width="561" height="159" fill="var(--navy-deep)" opacity="0.85"/>
      <text x="33" y="110" textLength="565" lengthAdjust="spacingAndGlyphs">410-937-2815</text>
    </svg>
  </div>

  <div class="brand">
    <div class="brand-mark"></div>
    <div class="brand-name">Brightmeadow<br>Homes Group</div>
  </div>

  <div class="legal">
    <div>Office: <strong>833-555-2947</strong></div>
    <div>2741 W Harrowgate Rd., Bel Air, MD 21014</div>
    <div class="web">www.brightmeadowhomes.com</div>
  </div>
</main>
</body>
</html>
```